Re-launching marine insurance adjusting company - looking for energy

I am a sole practitioner specializing in the profession of average adjusting. There is an on-line brochure at www.rkbtnova.com I am one of only a handful of specialists in this field and I enjoy a fair amount of name recognition, domestically in the US and internationally. My principal markets are the US, the London and Scandinavian insurance markets and shipowners and insurers in Latin America.
The business is a mixture of law, accounting and insurance and my clientele relies on a time-sensitive and accurate work-product, clearly stating an insurance company's liability for a given claim. The identity needs to project gravitas rather than flash.
Since 1998 I have traded as "The Halloway Company" but have also attempted to establish the name RKBNOVA.com so that people would visit my website.
I want to implement a single identity across my stationery, business cards and website. I have come to see "The Halloway Company" as rather fatuous, since there is no company, it is just me. The Internet domain RKBNOVA is long-established and I would be reluctant to change it. I have considered trading as simply Marcus T Halloway, MTH, RKBNOVA or attempting to come up with a name that could be abbreviated to MTH, e.g. M Halloway Trelantics - but I can't find a suitable word for the second S.
Logo-wise, I have considered a stylized MTH or RKBNOVA redolent of waves of the sea. A nautical theme embodying a cargo ship, navigational beacon or lighthouse might be appropriate but these tend to be hackneyed.
I have attached a card that I mocked up at Pix, connoting stacking up numbers, which I really like, but I think it is too cryptic for people in most insurance companies, who don't particularly think laterally or they wouldn't work in marine insurance, and the card that I use currently, which I intended to be understated, but in fact it states nothing.
I have also attached my current letterhead, to demonstrate how I really need help.
Finally, I have attached a credentials sheet, to attempt to establish how narrow and deep is the professional niche that I occupy.
What I am looking to implement is a single logo, font, them and color scheme to use across my website, letterhead and business cards.
Over to the Sketch Guild...
Target Market(s)
Ship owners and insurance companies
Industry/Entity Type
Accounting

```html
<!DOCTYPE html>
<html lang="en">
<head>
<meta charset="utf-8">
<title>RKBNOVA Letterhead</title>
<link rel="stylesheet" href="https://fonts.googleapis.com/css2?family=Carlito:wght@400;700&family=Poppins:wght@300;400&display=swap">
<style>
:root{
  --backdrop:#e2e2e2;
  --paper:#f8f8f8;
  --brand-red:#c2453f;
  --brand-red-deep:#b63c37;
  --ink:#2f2f2f;
  --ink-soft:#5a5a5a;
  --on-brand:#ffffff;
}
*{margin:0;padding:0;box-sizing:border-box}
html,body{width:1200px;height:1000px;overflow:hidden}
body{background:var(--backdrop);position:relative;font-family:"Carlito",Calibri,sans-serif;color:var(--ink)}

.brand-mark{position:absolute;font-family:"Carlito",Calibri,sans-serif;font-weight:700;color:var(--brand-red);line-height:1}
.brand-mark .wordmark{display:block;letter-spacing:2px}
.brand-mark .tagline{display:block;font-weight:700;letter-spacing:3.5px;margin-top:4px}
.brand-mark--standalone{left:62px;top:842px}
.brand-mark--standalone .wordmark{font-size:44px}
.brand-mark--standalone .tagline{font-size:10px;letter-spacing:4.3px;margin-left:18px}

.letterhead{position:absolute;left:400px;top:64px;width:618px;height:870px;background:var(--paper);overflow:hidden}

.letterhead .brand-mark{left:56px;top:42px}
.letterhead .brand-mark .wordmark{font-size:38px}
.letterhead .brand-mark .tagline{font-size:8.5px;margin-left:14px}

.header-divider{position:absolute;left:284px;top:35px;width:1.5px;height:60px;background:var(--brand-red)}
.contact{position:absolute;top:51px;font-family:"Poppins",sans-serif;font-weight:300;font-size:10.5px;line-height:13px;color:var(--ink-soft)}
.contact--address{left:306px}
.contact--phone{left:464px}

.sender{position:absolute;left:171px;top:184px;font-family:"Poppins",sans-serif;font-weight:300;line-height:15px;color:var(--ink)}
.sender .name{font-size:11.5px;font-weight:400}
.sender .role{font-size:10.5px;color:var(--ink-soft)}

.subject{position:absolute;left:172px;top:261px;font-size:12.5px;font-weight:700}

.aside-note{position:absolute;left:72px;top:293px;width:84px;text-align:right;font-size:12px;line-height:15px;color:var(--ink-soft)}
.aside-note strong{color:var(--ink)}

.letter-body{position:absolute;left:171px;top:293px;width:372px;font-size:12px;line-height:15px;text-align:justify;hyphens:auto;-webkit-hyphens:auto;color:var(--ink)}
.letter-body p{margin-bottom:15px}

.signature{position:absolute;left:172px;top:690px;width:118px;height:26px;background:linear-gradient(90deg,#ececec,#f3f3f3)}
.signature-name{position:absolute;left:173px;top:720px;font-size:11.5px}

.footer-band{position:absolute;left:0;bottom:0;width:618px;height:44px;background:linear-gradient(90deg,var(--brand-red-deep),var(--brand-red))}
.footer-contact{position:absolute;top:843px;font-family:"Poppins",sans-serif;font-weight:300;font-size:10.5px;color:var(--on-brand)}
.footer-contact--email{left:312px}
.footer-contact--web{left:470px}
</style>
</head>
<body>

<div class="brand-mark brand-mark--standalone">
  <span class="wordmark">RKBNOVA</span>
  <span class="tagline">The Halloway Company</span>
</div>

<main class="letterhead">
  <div class="brand-mark">
    <span class="wordmark">RKBNOVA</span>
    <span class="tagline">The Halloway Company</span>
  </div>
  <div class="header-divider"></div>
  <div class="contact contact--address">48 Harbor View Lane<br>New York, NY 10027, USA</div>
  <div class="contact contact--phone">Tel: (212) 555 0147<br>Fax: (212) 555 0182</div>

  <div class="sender">
    <div class="name">Marcus T. Halloway</div>
    <div class="role">Average Adjuster</div>
  </div>

  <h1 class="subject">Lorem ipsum dolor sit amet, ei eros vidit sonet eum</h1>

  <div class="aside-note"><strong>Lorem ipsum</strong><br>Dolor sit amet eros vidit sonet sed</div>

  <div class="letter-body">
    <p>Lorem ipsum dolor sit amet, ei eros vidit sonet eum, sed ea aliquam offendit. Reque quando labitur nec in, no solum ceteros est. Accumsan pertinacia an qui. Te vidisse recteque pro, cu per habemus officiis, eos ex malis posidonium omittantur. Appetere principes eloquentiam vis ei, an mea alia petentium dignissim, te justo omnium duo.</p>
    <p>Movet laoreet delicatissimi cum id. Essent dissentiet cu cum, atqui augue iriure qui ea. Liber propriae ei sed. Euismod ornatus scaevola et pro.</p>
    <p>Verterem interesset disputationi vim et, laudem persecuti quo eu. Mea viderer vulputate ut. Ad scripta scaevola appetere usu, omnium forensibus sed cu, dolorum admodum postulant mea ei. Eos ut ubique graeco insolens, etiam electram assentior cum at.</p>
    <p>In eos solum verterem facilisis, magna scaevola explicari has ex, at vidisse percipitur cum. At dicam postea luptatum sea, sed te timeam principes disputando, postea scaevola eloquentiam quo eu. Cetero concludaturque cu ius, nam erat detraxit ut, in his cetero vocent erroribus. Eu sint nulla comprehensam qui. Dolor dolorum splendide ei est, id usu inani liber deterruisset.</p>
    <p>Omnis intellegat intellegam duo cu, no ornatus partiendo referrentur has</p>
  </div>

  <div class="signature" role="img" aria-label="Handwritten signature of Marcus T. Halloway"></div>
  <div class="signature-name">Marcus T. Halloway</div>

  <div class="footer-band" role="img" aria-label="Decorative footer band in the brand red and blue"></div>
  <div class="footer-contact footer-contact--email">E-mail: info@rkbnova.com</div>
  <div class="footer-contact footer-contact--web">Web: www.rkbnova.com</div>
</main>

</body>
</html>
```